Companybrochure for Consulting & Financing Firm

I need to have a Company Brochure asap for our company. We have a website that describes what we do, but we need also a brochure, that can be sent by PDF of eventually be printed as well.

The brochure should be short but nice and appealing to the customers.

We provide professional management consulting and help our customers to get finance for very diferent projects. Our business has a lot to do with personal relations, but also we are very professional in the way we work and how develop the solutions for our clients. Our clients are mainly government-owned firm, but also private trading companies and wealthy private investors.

Our customers are mainly in Latin America, but the company is headquater is in Switzerland. We are opening offices in Panama and Caracas, this should be easaly be adabtable later.

Please have a look at our website www.brevalto.ch. In the brochure, we would segment our services in 1.) Project Developments 2.) Management Conulting 3.) Investment Management and 4.) Finance Solutions.

Also do have a look at www.brevalto.ch
(Click E for the English version)

I managed to put the Mock-Up to the Website.
It is actually not really a mock-up, it is a version I have designed myself.
Well as I am not a designer, I hope you can make it much better.
The content however is what I would put in any other design as well.

Target Market(s)

Top Management, Investors, Entrepreneurs, Government Officials

Industry/Entity Type

Management Consulting

Requirements
Must have
• Design should reflect this image elements:

We are entrepreneurs.
We are comitted to get things done.
We work closely with the client side by side.
We are a professional partner.
We are not afraid of delivering unconventional solutions.
We look at the problem from various angles.
We analyse, develop solutions and implent results.
Should not have
• Typical US-American style elements. We do not want to give the impression of being a US company.

We do not want to appear to be neo-liberal. We are a politically neutral professional consulting firm.

```html
<!DOCTYPE html>
<html lang="en">
<head>
<meta charset="utf-8">
<title>Brevalto AG – Brochure Spread</title>
<link href="https://fonts.googleapis.com/css2?family=Arimo:wght@400;700&family=Open+Sans:wght@400;600;700&display=swap" rel="stylesheet">
<style>
  :root {
    --canvas: #bcbec0;
    --navy: #3d4779;
    --navy-deep: #2e3a6e;
    --band-blue: #1aa0df;
    --panel-grey: #d3d4d6;
    --panel-light: #e6e7e8;
    --ink-navy: #3a4577;
    --ink-grey: #6d6e71;
    --heading: #3b4a72;
    --white: #ffffff;
  }
  * { box-sizing: border-box; margin: 0; padding: 0; }
  html, body { width: 1200px; height: 434px; overflow: hidden; }
  body { background: var(--canvas); position: relative; font-family: "Open Sans", Arial, sans-serif; }

  .page { position: absolute; top: 14px; height: 406px; background: var(--panel-grey); overflow: hidden; }
  .page--cover { left: 17px; width: 578px; }
  .page--service { left: 605px; width: 578px; }

  /* Cover */
  .cover-field { position: absolute; left: 0; top: 0; width: 100%; height: 221px; background: var(--navy); }
  .brand-name {
    position: absolute; right: 48px; top: 29px;
    font-family: "Arimo", Arial, sans-serif; font-weight: 700; font-size: 22px;
    color: var(--white); letter-spacing: 0.2px;
  }
  .tagline-band {
    position: absolute; left: 0; top: 221px; width: 100%; height: 58px;
    background: linear-gradient(90deg, var(--navy-deep) 0%, #2a63a8 25%, var(--band-blue) 52%, #2a63a8 74%, var(--navy-deep) 100%);
  }
  .tagline {
    position: absolute; left: 51px; top: 14px;
    font-family: "Arimo", Arial, sans-serif; font-weight: 700; font-size: 23px; color: var(--white);
  }
  .intro {
    position: absolute; left: 51px; top: 297px;
    font-weight: 700; font-size: 10.5px; line-height: 15.2px; color: var(--ink-navy);
  }
  .intro ul { list-style: none; }

  /* Service page */
  .photo { position: absolute; left: 0; top: 0; width: 100%; height: 208px; background: linear-gradient(90deg, #e4e6e8 0%, #cfd2d5 45%, #5a5d63 75%, #8a8c90 100%); }
  .photo-rule { position: absolute; left: 0; top: 208px; width: 100%; height: 14px; background: var(--navy); }
  .heading-band { position: absolute; left: 0; top: 222px; width: 100%; height: 39px; background: var(--panel-light); }
  .service-title {
    position: absolute; left: 51px; top: 8px;
    font-family: "Arimo", Arial, sans-serif; font-weight: 700; font-size: 19px; color: var(--heading);
  }
  .service-copy {
    position: absolute; left: 51px; top: 271px; width: 490px;
    font-size: 8.6px; line-height: 12.4px; color: var(--ink-grey);
  }
  .service-copy p + p { margin-top: 12.4px; }
</style>
</head>
<body>
  <section class="page page--cover">
    <div class="cover-field"></div>
    <div class="brand-name">Brevalto AG</div>
    <div class="tagline-band"><p class="tagline">&gt; Analyze &gt;&gt; Develop &gt;&gt;&gt; Deliver</p></div>
    <div class="intro">
      <p>We are a professional consulting, financing and<br>investment firm operating in the fields of:</p>
      <ul>
        <li>&gt; Project Development</li>
        <li>&gt; Management Consulting</li>
        <li>&gt; Investment Management</li>
        <li>&gt; Finance Solutions</li>
      </ul>
    </div>
  </section>

  <section class="page page--service">
    <div class="photo" role="img" aria-label="Photo of four business people in dark suits reviewing documents together in a bright office"></div>
    <div class="photo-rule"></div>
    <div class="heading-band"><h2 class="service-title">&gt;&gt; Project Development</h2></div>
    <div class="service-copy">
      <p>Sometimes a project with high potential has to be developed before its economic value becomes apparent.</p>
      <p>In such situations, we participate financially in the project and commit ourselves as entrepreneurs together<br>with the owners.</p>
      <p>We also take care of project management.</p>
    </div>
  </section>
</body>
</html>
```